VerintaCore PowerPoint Presentation Design

I am looking for a PowerPoint design for a new company based in Dallas, Texas called VerintaCore. We provide extremely powerful predictive and prescriptive analytics software focused on the Internet of Things (IoT) market. Our initial products are called VRC Foundry and VRC Pulse. We would like to see designs that support our logo design, which is attached.

I AM LOOKING FOR A THEME TO BE DEVELOPED FOR THE TITLE SLIDE AND INSIDE SLIDES OF A PRESENTATION. I AM NOT LOOKING FOR SOMEONE TO TAKE MY CONTENT AND CREATE A COMPLETE PRESENTATION.

Target Market(s)

Advanced Analytics, Internet of Things

Industry/Entity Type

It Company

Requirements
Must have
• Bolder colors, but they must work with the logo
Nice to have
• I prefer that the design incorporate the them of "connectivity" or "connectedness" to reflect the IoT market and "intelligence" or "smart" to reflect the analytics aspect of the business
Should not have
• I don't want people represented in the graphics scheme

```html
<!DOCTYPE html>
<html lang="en">
<head>
<meta charset="utf-8">
<title>About Us – VerintaCore</title>
<link href="https://fonts.googleapis.com/css2?family=Titillium+Web:wght@600;700&family=Ubuntu:wght@400;500&display=swap" rel="stylesheet">
<style>
  :root {
    --bg: #efeeef;
    --bg-soft: #e9e8ea;
    --ink: #111111;
    --brand-blue: #1b56a8;
    --accent-orange: #f5a100;
    --accent-yellow: #fbbf12;
    --body-grey: #555555;
    --sub-grey: #666666;
    --rule: #c9c9c9;
    --footer-blue: #2f56b5;
    --white: #ffffff;
  }
  * { margin: 0; padding: 0; box-sizing: border-box; }
  html, body { width: 1200px; height: 900px; overflow: hidden; background: var(--bg); }
  .slide {
    position: relative; width: 1200px; height: 900px; overflow: hidden;
    background: var(--bg);
    font-family: "Ubuntu", Arial, sans-serif;
  }
  .background-art {
    position: absolute; left: 0; top: 400px; width: 1200px; height: 400px;
    background: radial-gradient(ellipse at 50% 60%, var(--bg-soft) 0%, var(--bg) 70%);
  }
  .slide-title {
    position: absolute; left: 50px; top: 22px;
    font-family: "Titillium Web", Arial, sans-serif; font-weight: 700;
    font-size: 43px; letter-spacing: 1px; color: var(--ink); line-height: 1.1;
  }
  .slide-title .company { color: var(--brand-blue); }
  .title-rule { position: absolute; left: 50px; top: 78px; width: 492px; height: 1px; background: var(--rule); }
  .subtitle { position: absolute; left: 50px; top: 88px; font-size: 20px; color: var(--sub-grey); }
  .brand {
    position: absolute; right: 30px; top: 18px;
    font-family: "Titillium Web", Arial, sans-serif; font-weight: 600;
    font-size: 44px; color: var(--brand-blue); line-height: 1;
  }
  .point { position: absolute; left: 62px; width: 1110px; }
  .point-heading {
    display: flex; align-items: center; gap: 12px;
    font-size: 25px; font-weight: 500; color: var(--brand-blue); line-height: 1;
  }
  .point-heading svg { width: 28px; height: 30px; flex: none; }
  .point-text {
    margin-left: 40px; margin-top: 10px;
    font-size: 19.65px; color: var(--body-grey); line-height: 33px; width: 1070px;
  }
  .footer { position: absolute; left: 0; bottom: 0; width: 1200px; height: 63px; }
  .footer-svg { position: absolute; inset: 0; }
  .copyright { position: absolute; left: 14px; top: 20px; font-size: 20px; color: var(--white); letter-spacing: -0.3px; }
  .page-number { position: absolute; right: 26px; top: 20px; font-size: 20px; color: var(--white); }
</style>
</head>
<body>
<div class="slide">
  <div class="background-art" role="img" aria-label="Faint connected-nodes network graphic in the background"></div>

  <h1 class="slide-title">ABOUT US <span class="company">VERINTACORE</span></h1>
  <div class="title-rule"></div>
  <p class="subtitle">Subtext here Subtext here Subtext here</p>
  <div class="brand">VerintaCore</div>

  <section class="point" style="top:176px">
    <h2 class="point-heading"><svg viewBox="0 0 28 30"><path d="M4 2 L14 2 L25 15 L14 28 L4 28 L15 15 Z" fill="var(--accent-orange)"/></svg>Lorem ipsum dolor sit Lorem ipsum</h2>
    <p class="point-text">Lorem ipsum dolor sit Lorem ipsum dolor sit&nbsp; Lorem ipsum dolor sit Lorem ipsum dolor sit&nbsp; Lorem ipsum dolor sit Lorem ipsum dolor sit&nbsp; Lorem ipsum dolor sit Lorem ipsum dolor sit&nbsp; Lorem ipsum dolor sit Lorem ipsum dolor sit&nbsp; Lorem ipsum</p>
  </section>
  <section class="point" style="top:313px">
    <h2 class="point-heading"><svg viewBox="0 0 28 30"><path d="M4 2 L14 2 L25 15 L14 28 L4 28 L15 15 Z" fill="var(--accent-orange)"/></svg>Lorem ipsum dolor sit Lorem ipsum</h2>
    <p class="point-text">Lorem ipsum dolor sit Lorem ipsum dolor sit&nbsp; Lorem ipsum dolor sit Lorem ipsum dolor sit&nbsp; Lorem ipsum dolor sit Lorem ipsum dolor sit&nbsp; Lorem ipsum dolor sit Lorem ipsum dolor sit&nbsp; Lorem ipsum dolor sit Lorem ipsum dolor sit&nbsp; Lorem ipsum</p>
  </section>
  <section class="point" style="top:464px">
    <h2 class="point-heading"><svg viewBox="0 0 28 30"><path d="M4 2 L14 2 L25 15 L14 28 L4 28 L15 15 Z" fill="var(--accent-orange)"/></svg>Lorem ipsum dolor sit Lorem ipsum</h2>
    <p class="point-text">Lorem ipsum dolor sit Lorem ipsum dolor sit&nbsp; Lorem ipsum dolor sit Lorem ipsum dolor sit&nbsp; Lorem ipsum dolor sit Lorem ipsum dolor sit&nbsp; Lorem ipsum dolor sit Lorem ipsum dolor sit&nbsp; Lorem ipsum dolor sit Lorem ipsum dolor sit&nbsp; Lorem ipsum</p>
  </section>
  <section class="point" style="top:616px">
    <h2 class="point-heading"><svg viewBox="0 0 28 30"><path d="M4 2 L14 2 L25 15 L14 28 L4 28 L15 15 Z" fill="var(--accent-orange)"/></svg>Lorem ipsum dolor sit Lorem ipsum</h2>
    <p class="point-text">Lorem ipsum dolor sit Lorem ipsum dolor sit&nbsp; Lorem ipsum dolor sit Lorem ipsum dolor sit&nbsp; Lorem ipsum dolor sit Lorem ipsum dolor sit&nbsp; Lorem ipsum dolor sit Lorem ipsum dolor sit&nbsp; Lorem ipsum dolor sit Lorem ipsum dolor sit&nbsp; Lorem ipsum</p>
  </section>

  <footer class="footer">
    <svg class="footer-svg" width="1200" height="63" viewBox="0 0 1200 63" aria-hidden="true">
      <defs>
        <linearGradient id="footerBand" x1="0" y1="0" x2="1" y2="0">
          <stop offset="0" stop-color="var(--accent-orange)"/>
          <stop offset="1" stop-color="var(--accent-yellow)"/>
        </linearGradient>
      </defs>
      <polygon points="0,0 1058,0 1092,63 0,63" fill="url(#footerBand)"/>
      <polygon points="1078,0 1120,0 1148,63 1106,63" fill="var(--ink)"/>
      <polygon points="1130,0 1200,0 1200,63 1158,63" fill="var(--footer-blue)"/>
    </svg>
    <span class="copyright">Copyright text here</span>
    <span class="page-number">01</span>
  </footer>
</div>
</body>
</html>
```